Tranquil Harbor yoga, meditation & wellness

I teach kundalini yoga and meditation classes.
I have adult beginner classes, seniors classes, family yoga classes, kids yoga classes
I also offer events like cacao ceremony, full moon ceremony, and retreats

Professional, and simple website that is easy to navigate, and easy for me to update, change.

Target Market(s)

all ages

Industry/Entity Type

Health And Wellness

Coding

Coded - Design and coding required

Number of Pages Required

5+ page

Font styles to use
Decorative

Colors
cedeed
eedded
e4daeb
fbd4d5
fee3d4

Requirements
Must have
• tabs required: about, contact, events, classes, blog,
• I would like to link my facebook page & instagram accounts to the website
Nice to have
• I would like my clients to be able to register for classes and events from my website
• I would like to have a "shop" option in the future, for some items that I have for sale

```html
<!DOCTYPE html>
<html lang="en">
<head>
<meta charset="utf-8">
<title>Tranquil Harbor — Yoga, Meditation &amp; Wellness</title>
<link rel="stylesheet" href="https://fonts.googleapis.com/css2?family=Montserrat:wght@400;600;700;800&family=Roboto:wght@300;400;500&display=swap">
<style>
:root{
  --pink:#ef6f97;
  --pink-soft:#f6a0bc;
  --pink-pale:#fbd4d5;
  --blush:#fde8ea;
  --ink:#222;
  --text:#6b6b6b;
  --line:#e3e3e3;
  --dark:#2e2e2e;
  --white:#fff;
}
*{box-sizing:border-box;margin:0;padding:0}
html,body{width:1200px;height:4017px;overflow:hidden}
body{font-family:"Roboto",sans-serif;color:var(--text);background:var(--white);position:relative}
h1,h2,h3,h4,.caps{font-family:"Montserrat",sans-serif}
.btn{display:inline-flex;align-items:center;justify-content:center;border-radius:30px;font-family:"Montserrat",sans-serif;font-weight:600;font-size:12px;letter-spacing:.5px;text-transform:uppercase;white-space:nowrap}
.photo{position:absolute}
.eyebrow{font-family:"Montserrat",sans-serif;font-size:12px;font-weight:600;color:var(--pink);letter-spacing:1px;text-transform:uppercase;text-align:center}
.section-title{font-family:"Montserrat",sans-serif;font-weight:800;font-size:27px;color:var(--ink);text-align:center;text-transform:uppercase}
.lede{font-size:14px;line-height:24px;text-align:center;color:var(--text)}

/* hero */
.hero{position:absolute;left:0;top:0;width:1200px;height:547px;background:linear-gradient(180deg,#f07aa2 0%,#f38cac 60%,#f6a2bd 100%)}
.logo{position:absolute;left:140px;top:32px;display:flex;align-items:center;gap:10px;color:var(--white);font-family:"Montserrat",sans-serif;font-weight:600;font-size:19px}
.logo .dot{width:14px;height:14px;border-radius:50%;background:var(--white)}
.nav{position:absolute;left:414px;top:41px;width:322px;display:flex;justify-content:space-between;font-family:"Montserrat",sans-serif;font-size:11px;font-weight:600;color:var(--white);white-space:nowrap}
.phone-pill{position:absolute;left:763px;top:28px;width:146px;height:36px;border:1.5px solid var(--white);color:var(--white);font-size:12px;gap:8px;border-radius:30px;display:flex;align-items:center;justify-content:center;font-family:"Montserrat",sans-serif;font-weight:600;white-space:nowrap}
.register{position:absolute;left:924px;top:29px;width:142px;height:34px;background:var(--white);color:var(--pink)}
.hero h1{position:absolute;left:152px;top:226px;font-size:38px;font-weight:800;color:var(--white);letter-spacing:1px;white-space:nowrap}
.hero p{position:absolute;left:152px;top:286px;width:420px;font-size:13px;line-height:24px;color:var(--white)}
.hero .learn{position:absolute;left:152px;top:358px;width:120px;height:38px;border:1.5px solid var(--white);color:var(--white)}
.hero .join{position:absolute;left:288px;top:358px;width:120px;height:38px;background:var(--white);color:var(--pink)}
.hero-photo{left:660px;top:80px;width:380px;height:467px;background:radial-gradient(ellipse at 50% 55%,#f4efeb 0%,#f2d9dd 40%,rgba(246,162,189,0) 72%)}

/* about */
.about{position:absolute;top:547px;left:0;width:1200px;height:466px}
.about .eyebrow{position:absolute;top:60px;width:100%}
.about .section-title{position:absolute;top:86px;width:100%}
.about .lede{position:absolute;top:130px;left:350px;width:500px}
.class-card{position:absolute;top:224px}
.class-card h3{font-size:15px;font-weight:700;color:var(--ink);margin-bottom:10px}
.class-card p{font-size:12px;line-height:20px}
.ring{position:absolute;width:180px;height:180px;border-radius:50%;border:8px solid var(--pink-pale);background:linear-gradient(160deg,#e9e3e0,#c9bcb8)}
.btn-soft{background:var(--pink-pale);color:var(--ink);width:92px;height:30px;font-size:11px;margin-top:18px}

/* teacher */
.teacher{position:absolute;top:1013px;left:0;width:1200px;height:440px;background:var(--pink-pale)}
.portrait{left:173px;top:46px;width:375px;height:375px;border-radius:50%;border:10px solid var(--white);background:radial-gradient(circle at 50% 45%,#e5c8b4,#b89886 60%,#7b6a62)}
.teacher .eyebrow{position:absolute;left:578px;top:64px;text-align:left;color:var(--ink)}
.teacher h2{position:absolute;left:578px;top:98px;font-size:20px;font-weight:700;color:var(--ink)}
.teacher .bio{position:absolute;left:578px;top:146px;width:430px;font-size:12px;line-height:21px;color:var(--text)}
.teacher .bio p+p{margin-top:14px}
.teacher .more{position:absolute;left:578px;top:358px;width:108px;height:32px;background:var(--white);color:var(--ink)}

/* explore */
.explore{position:absolute;top:1453px;left:0;width:1200px;height:424px}
.explore-bg{left:0;top:0;width:1200px;height:424px;background:linear-gradient(180deg,#fff 0%,#f6f5f4 55%,#ecebea 100%)}
.explore .eyebrow{position:absolute;top:46px;width:100%}
.explore .section-title{position:absolute;top:70px;width:100%;font-size:25px}
.class-tile{position:absolute;top:144px;width:210px}
.class-tile .img{width:210px;height:130px;background:linear-gradient(160deg,#d8cfc7,#a99b90)}
.class-tile .img.hover{background:var(--pink-pale);display:flex;align-items:center;justify-content:center}
.class-tile .img.hover span{font-family:"Montserrat",sans-serif;font-size:10px;font-weight:600;color:var(--ink);background:var(--white);padding:6px 12px;border-radius:20px}
.class-tile h4{margin-top:14px;font-size:11px;font-weight:700;color:var(--ink);text-transform:uppercase}
.class-tile p{margin-top:6px;font-size:11.5px;line-height:18px}

/* events */
.events{position:absolute;top:1877px;left:0;width:1200px;height:440px}
.events-bg{left:0;top:0;width:1200px;height:440px;background:linear-gradient(180deg,#3a3433 0%,#262424 50%,#1f1d1d 100%)}
.events .section-title{position:absolute;top:78px;width:100%;color:var(--pink)}
.events .lede{position:absolute;top:118px;width:100%;color:var(--white);font-size:13px}
.event{position:absolute;top:172px;width:302px;text-align:center}
.event .img{width:302px;height:156px}
.event h4{margin-top:20px;font-size:14px;font-weight:700;color:var(--white);text-transform:uppercase}

/* member */
.member{position:absolute;top:2317px;left:0;width:1200px;height:288px}
.member-bg{left:0;top:0;width:1200px;height:288px;background:linear-gradient(90deg,#e9a9b9 0%,#f4d3da 30%,#f8e3e6 60%,#f2d6dc 100%)}
.member h2{position:absolute;top:70px;width:100%;text-align:center;font-size:29px;font-weight:700;color:var(--ink)}
.member p{position:absolute;top:124px;left:400px;width:400px;text-align:center;font-size:12px;line-height:20px}
.member .join{position:absolute;top:184px;left:540px;width:120px;height:36px;background:var(--pink);color:var(--white)}

/* products */
.products{position:absolute;top:2605px;left:0;width:1200px;height:518px}
.products .section-title{position:absolute;top:42px;width:100%;font-size:21px}
.arrow{position:absolute;top:205px}
.product{position:absolute;top:106px;width:219px;text-align:center}
.product .card{width:219px;height:218px;border:1px solid var(--line);display:flex;align-items:center;justify-content:center}
.product .card.active{background:var(--pink-pale);border:4px solid #f7c0c8}
.product .shape{width:140px;height:140px}
.product h4{margin-top:22px;font-family:"Roboto",sans-serif;font-size:14px;font-weight:400;color:var(--ink)}
.product .price{margin-top:8px;font-size:15px;color:var(--ink)}
.product .cart{margin:18px auto 0;width:134px;height:30px;border:1px solid #bdbdbd;border-radius:2px;color:var(--ink);font-size:11px;font-weight:500}
.product .cart.on{background:var(--pink-pale);border-color:var(--pink-pale)}
.divider{position:absolute;left:132px;top:515px;width:936px;height:1px;background:var(--line)}

/* blog */
.blog{position:absolute;top:3123px;left:0;width:1200px;height:570px}
.blog .section-title{position:absolute;top:32px;width:100%;font-size:25px}
.post{position:absolute;top:100px;width:308px;height:408px;border:1px solid var(--line);text-align:center;padding:0 14px}
.post.featured{border-color:var(--pink-soft)}
.post .date{margin-top:6px;font-size:11px;color:#999}
.post .img{margin-top:10px;width:278px;height:186px;background:linear-gradient(160deg,#e4d4cc,#b09c92)}
.post h4{margin-top:28px;font-size:12.5px;font-weight:700;color:var(--ink);text-transform:uppercase}
.post p{margin-top:12px;font-size:11.5px;line-height:18px}

/* footer */
.footer{position:absolute;top:3693px;left:0;width:1200px;height:324px;background:var(--dark);color:#cfcfcf}
.footer .brand{position:absolute;left:150px;top:74px;color:var(--pink-pale);font-family:"Montserrat",sans-serif;font-weight:600;font-size:15px;display:flex;align-items:center;gap:8px;white-space:nowrap}
.footer .brand .dot{width:12px;height:12px;border-radius:50%;background:var(--pink-pale)}
.footer h5{font-family:"Montserrat",sans-serif;font-size:12px;font-weight:700;color:var(--white);letter-spacing:1px;text-transform:uppercase}
.contact-col{position:absolute;left:325px;top:76px}
.contact-col li{list-style:none;display:flex;gap:14px;font-size:12px;line-height:18px;margin-top:12px;align-items:flex-start}
.contact-col li svg{flex:none;margin-top:2px}
.links-col{position:absolute;left:607px;top:76px}
.links-col .cols{display:flex;gap:48px;margin-top:18px}
.links-col ul{list-style:none;font-size:12px;line-height:30px}
.follow-col{position:absolute;left:835px;top:76px}
.socials{display:flex;gap:30px;margin-top:28px}
.socials span{width:14px;height:14px;border-radius:50%;background:#cfcfcf}
.copyright{position:absolute;bottom:20px;width:100%;text-align:center;font-size:11px;color:#8a8a8a}
</style>
</head>
<body>

<header class="hero">
  <div class="logo"><span class="dot"></span>Tranquil Harbor</div>
  <nav class="nav"><span>ABOUT</span><span>CONTACT</span><span>EVENTS</span><span>CLASSES</span><span>BLOG</span></nav>
  <div class="phone-pill">
    <svg width="12" height="12" viewBox="0 0 24 24" fill="#fff"><path d="M6.6 10.8a15 15 0 0 0 6.6 6.6l2.2-2.2c.3-.3.7-.4 1-.2 1.1.4 2.3.6 3.6.6.6 0 1 .4 1 1V20c0 .6-.4 1-1 1A17 17 0 0 1 3 4c0-.6.4-1 1-1h3.5c.6 0 1 .4 1 1 0 1.3.2 2.5.6 3.6.1.3 0 .7-.2 1z"/></svg>
    555-0142-880
  </div>
  <span class="btn register">Register Now</span>
  <h1>EXPLORE YOUR BEST SELF</h1>
  <p>Lorem Ipsum is simply dummy text of the printing and typesetting industry has been the industry's standard dummy text.</p>
  <span class="btn learn">Learn More</span>
  <span class="btn join">Join Now</span>
  <div class="photo hero-photo" role="img" aria-label="Teacher seated cross-legged in meditation, dressed in white"></div>
</header>

<section class="about">
  <div class="eyebrow">About Us</div>
  <h2 class="section-title">What do you get in our classes</h2>
  <p class="lede">Lorem Ipsum is simply dummy text of the printing and typesetting industry has been the industry's standard dummy text ever since the been when an unknown printer.</p>

  <div class="class-card" style="left:135px;width:210px;text-align:right">
    <h3>Kundalini Yoga</h3>
    <p>Kundalini Yoga comes from northern India and combines long traditions. It was brought to the West by a visiting teacher long ago.</p>
    <span class="btn btn-soft">View More</span>
  </div>
  <div class="ring" style="left:372px;top:222px" role="img" aria-label="Photo of a kundalini yoga practice"></div>

  <div class="ring" style="left:633px;top:222px" role="img" aria-label="Photo of a group meditation class"></div>
  <div class="class-card" style="left:836px;width:210px">
    <h3>Meditation Classes</h3>
    <p>Lorem Ipsum is simply dummy text of the printing and typesetting industry has been the industry's.</p>
    <span class="btn btn-soft">View More</span>
  </div>
</section>

<section class="teacher">
  <div class="photo portrait" role="img" aria-label="Portrait of the teacher"></div>
  <div class="eyebrow">Your Teacher</div>
  <h2>MIRA (SAT JOT KAUR)</h2>
  <div class="bio">
    <p>I have been practicing yoga for about 8 years. I began practicing Kundalini yoga 3 years ago, and it ignited a complete transformation of mind, body and spirit. I knew that I would go on to teach this lineage.</p>
    <p>I'm also a home-care nurse, my 15 years of health care experience has been invaluable. My most important job of all is wife, mother and home educator to my four daughters, ages 9-4 years. A typical part of Kundalini Yoga is a dynamic or flowing exercise series, beside quiet posture-holding exercises.</p>
  </div>
  <span class="btn more">Read More</span>
</section>

<section class="explore">
  <div class="photo explore-bg" role="img" aria-label="Misty mountain landscape, faded"></div>
  <div class="eyebrow">Why Help You?</div>
  <h2 class="section-title">Explore our classes</h2>

  <div class="class-tile" style="left:130px">
    <div class="img" role="img" aria-label="Adults practicing yoga on mats"></div>
    <h4>Adult Beginner Classes</h4>
    <p>Lorem ipsum dolor sit amet, consectetur adipiscing elit. In sit amet purus et</p>
  </div>
  <div class="class-tile" style="left:369px">
    <div class="img hover"><span>MORE DETAILS</span></div>
    <h4>Seniors Classes</h4>
    <p>Lorem ipsum dolor sit amet, consectetur adipiscing elit. In sit amet purus et</p>
  </div>
  <div class="class-tile" style="left:619px">
    <div class="img" role="img" aria-label="Family stretching together on yoga mats"></div>
    <h4>Family Yoga Classes</h4>
    <p>Lorem ipsum dolor sit amet, consectetur adipiscing elit. In sit amet purus et</p>
  </div>
  <div class="class-tile" style="left:858px">
    <div class="img" role="img" aria-label="Children in a yoga class"></div>
    <h4>Kids Yoga Classes</h4>
    <p>Lorem ipsum dolor sit amet, consectetur adipiscing elit. In sit amet purus et</p>
  </div>
</section>

<section class="events">
  <div class="photo events-bg" role="img" aria-label="Dimmed photo of a yoga class in a studio"></div>
  <h2 class="section-title">We offer events</h2>
  <p class="lede">Lorem ipsum dolor sit amet, consectetur adipiscing elit. In sit amet purus et</p>
  <div class="event" style="left:130px">
    <div class="img" role="img" aria-label="Cacao ceremony gathering outdoors" style="background:linear-gradient(160deg,#8a6f5e,#3f2f28)"></div>
    <h4>Cacao Ceremony</h4>
  </div>
  <div class="event" style="left:450px">
    <div class="img" role="img" aria-label="Full moon over a tree at dusk" style="background:linear-gradient(180deg,#2a3550 0%,#6b5c78 55%,#e79a5a 85%,#2a2020 100%)"></div>
    <h4>Full Moon Ceremony</h4>
  </div>
  <div class="event" style="left:770px">
    <div class="img" role="img" aria-label="Group retreat in a forest" style="background:linear-gradient(160deg,#9aa184,#4d5240)"></div>
    <h4>Retreats</h4>
  </div>
</section>

<section class="member">
  <div class="photo member-bg" role="img" aria-label="Woman meditating before a misty mountain landscape, pink tint"></div>
  <h2>Become a&nbsp; Yoga Member</h2>
  <p>Lorem ipsum dolor sit amet, consectetur adipiscing elit. In sit amet purus et nunc porta fringilla. Maecenas volutpat fermentum ante.</p>
  <span class="btn join">Join Now</span>
</section>

<section class="products">
  <h2 class="section-title">Featured Prodcuts Section</h2>
  <svg class="arrow" style="left:98px" width="14" height="22" viewBox="0 0 14 22"><path d="M12 2 3 11l9 9" fill="none" stroke="#e8a05a" stroke-width="2"/></svg>
  <svg class="arrow" style="left:1090px" width="14" height="22" viewBox="0 0 14 22"><path d="m2 2 9 9-9 9" fill="none" stroke="#e8a05a" stroke-width="2"/></svg>

  <div class="product" style="left:132px">
    <div class="card active"><div class="shape" role="img" aria-label="White sports top" style="background:linear-gradient(180deg,#fbeeee,#f1dada)"></div></div>
    <h4>Winter Jacket</h4><div class="price">$ 149.99</div>
    <span class="btn cart">Add to Card</span>
  </div>
  <div class="product" style="left:377px">
    <div class="card"><div class="shape" role="img" aria-label="Red yoga bolster cushion" style="background:linear-gradient(160deg,#b0343f,#6e1a22)"></div></div>
    <h4>Winter Jacket</h4><div class="price">$ 65.99</div>
    <span class="btn cart">Add to Card</span>
  </div>
  <div class="product" style="left:619px">
    <div class="card"><div class="shape" role="img" aria-label="Blue yoga mat set" style="background:linear-gradient(160deg,#3a78c8,#1d4686)"></div></div>
    <h4>Winter Jacket</h4><div class="price">$ 109.99</div>
    <span class="btn cart on">Add to Card</span>
  </div>
  <div class="product" style="left:863px">
    <div class="card"><div class="shape" role="img" aria-label="Singing bowl with mallet" style="background:linear-gradient(160deg,#c59a58,#3f2f27)"></div></div>
    <h4>Winter Jacket</h4><div class="price">$ 69.99</div>
    <span class="btn cart">Add to Card</span>
  </div>
  <div class="divider"></div>
</section>

<section class="blog">
  <h2 class="section-title">Our Blog</h2>
  <article class="post featured" style="left:132px">
    <div class="date">June 24, 2018</div>
    <div class="img" role="img" aria-label="Group fitness class in a gym"></div>
    <h4>Why should go to Calmwell</h4>
    <p>We continue to maintain an alternative price "Top 10", and show a decent idea of the week, which were not the winners in the nomination "The best selection." Our "Trump" can be found in all the other words...</p>
  </article>
  <article class="post" style="left:460px">
    <div class="date">June 15, 2018</div>
    <div class="img" role="img" aria-label="Children stretching in a yoga class"></div>
    <h4>Yoga stretch your body &amp; mind</h4>
    <p>We continue to maintain an alternative price "Top 10", and show a decent idea of the week that are not become winners.</p>
  </article>
  <article class="post" style="left:786px">
    <div class="date">June 06, 2018</div>
    <div class="img" role="img" aria-label="Couple doing partner yoga"></div>
    <h4>Benifits yoga for gentleman</h4>
    <p>In the manufacture of concrete furniture in the first place, you need to make the formwork of casting objects. First you need to fill a form, which can be made of laminated chipboard...</p>
  </article>
</section>

<footer class="footer">
  <div class="brand"><span class="dot"></span>Tranquil Harbor</div>
  <div class="contact-col">
    <h5>Get in Touch</h5>
    <ul>
      <li><svg width="12" height="12" viewBox="0 0 24 24" fill="#cfcfcf"><path d="M6.6 10.8a15 15 0 0 0 6.6 6.6l2.2-2.2c.3-.3.7-.4 1-.2 1.1.4 2.3.6 3.6.6.6 0 1 .4 1 1V20c0 .6-.4 1-1 1A17 17 0 0 1 3 4c0-.6.4-1 1-1h3.5c.6 0 1 .4 1 1 0 1.3.2 2.5.6 3.6.1.3 0 .7-.2 1z"/></svg>555-0142-880</li>
      <li><svg width="12" height="12" viewBox="0 0 24 24" fill="#cfcfcf"><path d="M12 2a7 7 0 0 0-7 7c0 5 7 13 7 13s7-8 7-13a7 7 0 0 0-7-7zm0 9.5A2.5 2.5 0 1 1 12 6.5a2.5 2.5 0 0 1 0 5z"/></svg><span>42 Willow Lane<br>Harbor Bay 1020</span></li>
      <li><svg width="12" height="12" viewBox="0 0 24 24" fill="#cfcfcf"><path d="M2 5h20v14H2zm2 2v.5l8 5 8-5V7l-8 5z"/></svg>hello@tranquilharbor.example</li>
    </ul>
  </div>
  <div class="links-col">
    <h5>Useful Links</h5>
    <div class="cols">
      <ul><li>About</li><li>Contact</li><li>Events</li></ul>
      <ul><li>Classes</li><li>Blog</li></ul>
    </div>
  </div>
  <div class="follow-col">
    <h5>Follow Us</h5>
    <div class="socials"><span></span><span></span><span></span><span></span></div>
  </div>
  <div class="copyright">Copyright 2018 Tranquil Harbor. All Rights Reserved.</div>
</footer>

</body>
</html>
```